Bright Lantern Media Works Brochure

We need a DOUBLE GATE FOLD 4 PANEL brochure for our video production company. The brochure will show pics of our green screen studio, some post production images "like the weatherman" standing in front of a weather map, and descriptions of our services and pricing. I really want this to look professional and classy. I will upload photos I want to use.
Updates

Reason: Never mind. I cannot extend it 5 days. Just refund my money since no one has submitted a design.

Reason: We need a better design than what we have gotten. Half the submissions didn't even give us a gate fold as instructed.

Target Market(s)

The main target of our company is physicians and other medical professionals. More men than women.

Industry/Entity Type

It Company

Font styles to use
Serif
Sans Serif

Requirements
Must have
• Professional, high end.
Colors - the logo is on black. I would try to make the brochure black so the colors and images pop off the page. Our colors are blue and white as in the logo.
Nice to have
• It should be able to be mailed so the ouside back should be white with a place for a label to be attached.

```html
<!DOCTYPE html>
<html lang="en">
<head>
<meta charset="utf-8">
<title>Bright Lantern Media Works — Gate Fold Brochure</title>
<link href="https://fonts.googleapis.com/css2?family=Raleway:wght@400;500;600;700;800&display=swap" rel="stylesheet">
<style>
  :root {
    --stage: #dcc48e;
    --panel-black: #0b0b0b;
    --panel-black-soft: #1c1c1c;
    --gold: #e9dca8;
    --gold-deep: #c8b574;
    --cream: #f3ecd0;
    --white: #ffffff;
    --brand-blue: #3fb7e6;
    --grid-gray: #dedede;
    --grid-gray-light: #f2f2f2;
    --caption-ink: #222222;
    --frame: #2a2a2a;
    --band: #1a1a1a;
  }
  * { box-sizing: border-box; margin: 0; padding: 0; }
  html, body { width: 1200px; height: 800px; overflow: hidden; }
  body {
    background: var(--stage);
    font-family: "Raleway", sans-serif;
    position: relative;
  }
  .brochure {
    position: absolute;
    left: 50px; top: 60px;
    width: 1100px; height: 680px;
    display: grid;
    grid-template-columns: 290px 530px 280px;
    grid-template-rows: 606px 74px;
    box-shadow: 0 14px 30px rgba(0,0,0,.28);
  }
  .panel { position: relative; overflow: hidden; }
  .panel--about, .panel--services {
    background: linear-gradient(180deg, var(--panel-black-soft), var(--panel-black) 30%);
    color: var(--white);
  }
  .panel--about { padding: 30px 24px 0 30px; display: flex; flex-direction: column; }
  .about-title {
    font-weight: 700; font-size: 44px; letter-spacing: 2px;
    color: var(--gold); line-height: 1;
  }
  .about-rule {
    height: 2px; width: 170px; margin-top: 8px;
    background: linear-gradient(90deg, var(--gold-deep), var(--gold), transparent);
  }
  .brand {
    display: flex; align-items: center; justify-content: center; gap: 8px;
    margin: 28px 0 20px;
  }
  .brand-dot { width: 12px; height: 12px; border-radius: 50%; background: var(--brand-blue); flex: none; }
  .brand-name { font-weight: 600; font-size: 14px; color: var(--brand-blue); white-space: nowrap; }
  .subtitle {
    font-weight: 700; font-size: 20px; color: var(--cream);
    text-align: center; margin-bottom: 10px;
  }
  .body-copy { font-size: 12px; line-height: 1.28; color: var(--white); font-weight: 500; }
  .panel--about .body-copy { position: relative; z-index: 1; }
  .about-photo {
    position: absolute; left: 0; right: 0; bottom: 0; height: 108px;
    background: linear-gradient(180deg, #3a2b1c 0%, #7a5632 55%, #b07a44 100%);
  }
  .about-photo::before {
    content: ""; position: absolute; left: 0; right: 0; top: -28px; height: 40px;
    background: var(--panel-black);
    clip-path: polygon(0 0, 100% 0, 100% 30%, 0 100%);
  }

  .panel--gallery {
    background: linear-gradient(180deg, var(--grid-gray-light), var(--grid-gray));
    padding: 8px 14px;
    display: grid;
    grid-template-columns: 1fr 1fr;
    grid-template-rows: 132px 132px 132px 1fr;
    column-gap: 16px; row-gap: 10px;
  }
  .tile { display: flex; flex-direction: column; min-height: 0; }
  .tile-photo { flex: 1; border: 2px solid var(--frame); border-bottom: none; }
  .tile-caption {
    background: var(--white); border: 2px solid var(--frame); border-top: none;
    font-size: 9.5px; line-height: 1.2; color: var(--caption-ink);
    padding: 2px 5px 3px; font-weight: 500;
  }
  .tile--tall .tile-photo { border-bottom: 2px solid var(--frame); flex: none; height: 124px; }
  .tile--tall .tile-caption { background: transparent; border: none; padding-top: 6px; }
  .photo-white-studio { background: linear-gradient(180deg, #c9c3b8, #f4f2ee 60%, #d8d4cc); }
  .photo-cyc-studio { background: linear-gradient(180deg, #5a5a5a 0%, #a8a8a8 30%, #f1f1f1 70%, #d6d6d6); }
  .photo-green-screen { background: linear-gradient(135deg, #1f7a3c, #2fa655 60%, #1a5a30); }
  .photo-control-room { background: linear-gradient(180deg, #241a12, #5a3f26 55%, #9a6b3d); }

  .panel--services { padding: 30px 22px 0 20px; }
  .panel--services .subtitle { margin-bottom: 16px; }
  .service-tile { margin-top: 22px; }
  .service-tile + .service-tile { margin-top: 14px; }
  .service-photo { height: 90px; border: 2px solid var(--frame); }
  .service-caption { font-size: 9.5px; line-height: 1.2; color: var(--cream); padding-top: 4px; font-weight: 500; }

  .contact-band {
    grid-column: 1 / -1;
    background:
      repeating-linear-gradient(45deg, rgba(255,255,255,.04) 0 2px, transparent 2px 10px),
      repeating-linear-gradient(-45deg, rgba(255,255,255,.04) 0 2px, transparent 2px 10px),
      var(--band);
    border-top: 3px solid var(--gold-deep);
    display: flex; align-items: center; justify-content: space-between;
    padding: 0 40px 0 30px;
    color: var(--cream); font-weight: 600;
  }
  .contact-item { display: flex; align-items: center; gap: 10px; font-size: 14px; }
  .contact-item--phone { font-size: 22px; font-weight: 700; letter-spacing: 1px; }
  .contact-icon { width: 18px; height: 18px; flex: none; }
</style>
</head>
<body>
  <main class="brochure">
    <section class="panel panel--about">
      <h1 class="about-title">ABOUT</h1>
      <div class="about-rule"></div>
      <div class="brand">
        <span class="brand-dot"></span>
        <span class="brand-name">Bright Lantern Media Works</span>
      </div>
      <h2 class="subtitle">Subtitle</h2>
      <p class="body-copy">Lorem ipsum dolor sit amet, consectetur adipisicing elit, sed do eiusmod tempor incididunt ut labore et dolore magna aliqua. Ut enim ad minim veniam, quis nostrud exercitation ullamco laboris nisi ut aliquip ex ea commodo consequat. Duis aute irure dolor in reprehenderit in voluptate velit esse cillum dolore eu fugiat nulla pariatur. Excepteur sint occaecat cupidatat non proident, sunt in culpa qui officia deserunt mollit anim id est laborum</p>
      <div class="about-photo" role="img" aria-label="Audio mixing console in a wood-floored control room"></div>
    </section>

    <section class="panel panel--gallery">
      <figure class="tile"><div class="tile-photo photo-white-studio" role="img" aria-label="White backdrop studio with softbox lights"></div><figcaption class="tile-caption">Lorem ipsum dolor sit amet, consectetur adipisicing elit, sed do eiusmod tempor incididunt ut labore et dolore</figcaption></figure>
      <figure class="tile"><div class="tile-photo photo-cyc-studio" role="img" aria-label="Large white cyclorama studio with umbrella light"></div><figcaption class="tile-caption">Lorem ipsum dolor sit amet, consectetur adipisicing elit, sed do eiusmod tempor incididunt ut labore et dolore</figcaption></figure>
      <figure class="tile"><div class="tile-photo photo-cyc-studio" role="img" aria-label="Large white cyclorama studio with umbrella light"></div><figcaption class="tile-caption">Lorem ipsum dolor sit amet, consectetur adipisicing elit, sed do eiusmod tempor incididunt ut labore et dolore</figcaption></figure>
      <figure class="tile"><div class="tile-photo photo-white-studio" role="img" aria-label="White backdrop studio with softbox lights"></div><figcaption class="tile-caption">Lorem ipsum dolor sit amet, consectetur adipisicing elit, sed do eiusmod tempor incididunt ut labore et dolore</figcaption></figure>
      <figure class="tile"><div class="tile-photo photo-white-studio" role="img" aria-label="White backdrop studio with softbox lights"></div><figcaption class="tile-caption">Lorem ipsum dolor sit amet, consectetur adipisicing elit, sed do eiusmod tempor incididunt ut labore et dolore</figcaption></figure>
      <figure class="tile"><div class="tile-photo photo-cyc-studio" role="img" aria-label="Large white cyclorama studio with umbrella light"></div><figcaption class="tile-caption">Lorem ipsum dolor sit amet, consectetur adipisicing elit, sed do eiusmod tempor incididunt ut labore et dolore</figcaption></figure>
      <figure class="tile tile--tall"><div class="tile-photo photo-green-screen" role="img" aria-label="Presenter in a suit standing in front of a green screen"></div><figcaption class="tile-caption">Lorem ipsum dolor sit amet, consectetur adipisicing elit, sed do eiusmod tempor incididunt ut labore et dolore</figcaption></figure>
      <figure class="tile tile--tall"><div class="tile-photo photo-control-room" role="img" aria-label="Post production control room with mixing console"></div><figcaption class="tile-caption">Lorem ipsum dolor sit amet, consectetur adipisicing elit, sed do eiusmod tempor incididunt ut labore et dolore</figcaption></figure>
    </section>

    <section class="panel panel--services">
      <h2 class="subtitle">Subtitle</h2>
      <p class="body-copy">Lorem ipsum dolor sit amet, consectetur adipisicing elit, sed do eiusmod tempor incididunt ut labore et dolore magna aliqua. Ut enim ad minim veniam, quis nostrud exercitation ullamco laboris nisi ut aliquip ex ea commodo consequat. Duis aute irure dolor in reprehenderit in voluptate velit esse cillum dolore eu fugiat nulla pariatur. Excepteur sint occaecat cupidatat non proident, sunt in culpa qui officia deserunt mollit anim id est laborum</p>
      <figure class="service-tile"><div class="service-photo photo-cyc-studio" role="img" aria-label="Large white cyclorama studio"></div><figcaption class="service-caption">Lorem ipsum dolor sit amet, consectetur adipisicing elit, sed do eiusmod tempor incididunt ut labore et dolore</figcaption></figure>
      <figure class="service-tile"><div class="service-photo photo-control-room" role="img" aria-label="Post production control room with mixing console"></div><figcaption class="service-caption">Lorem ipsum dolor sit amet, consectetur adipisicing elit, sed do eiusmod tempor incididunt ut labore et dolore</figcaption></figure>
    </section>

    <footer class="contact-band">
      <div class="contact-item">
        <svg class="contact-icon" viewBox="0 0 20 20" fill="none" stroke="currentColor" stroke-width="1.6"><circle cx="10" cy="10" r="8"/><ellipse cx="10" cy="10" rx="3.5" ry="8"/><path d="M2 10h16M3.5 6h13M3.5 14h13"/></svg>
        <span>www.websiteaddress.com</span>
      </div>
      <div class="contact-item">
        <svg class="contact-icon" viewBox="0 0 20 20" fill="currentColor"><path d="M2 4h16v12H2z"/><path d="M2 4l8 7 8-7" fill="none" stroke="#1a1a1a" stroke-width="1.5"/></svg>
        <span>email@websiteaddress.com</span>
      </div>
      <div class="contact-item contact-item--phone">
        <svg class="contact-icon" viewBox="0 0 20 20" fill="currentColor"><path d="M5 2l3 4-2 2c1 2.5 3.5 5 6 6l2-2 4 3-2 3C9 18 2 11 2 4z"/></svg>
        <span>1234 5678 901</span>
      </div>
    </footer>
  </main>
</body>
</html>
```